Business cards, stationery, fax/email cover etc for dental office
Maple Hollow Dental Care
Business cards, stationery, fax/email cover etc  for dental office - Health
Creative Brief
Use standard fonts
any fonts that looks professional
Simple
418 Dunmore Avenue East Kitchener, Ontario N2H 4K7
mhdental@brisketmail.example
www.maplehollowdentalcare.example
we have three dentists in our practice. Dr. Mark Esler, Dr. Noreen Fadlallah, and Dr. Beatrice Holloway and Associates
Please make the back as appointment card with the following wording: "This time is reserved just for you. If you are unable to keep this appointment, you are responsible for notifying us immediately at least 24 business hours in advance in which case no charge will be made."

```html
<!DOCTYPE html>
<html lang="en">
<head>
<meta charset="utf-8">
<title>Maple Hollow Dental Care — Stationery</title>
<link rel="stylesheet" href="https://fonts.googleapis.com/css2?family=Cinzel:wght@400;600&family=Lato:wght@300;400;700&display=swap">
<style>
  :root {
    --bg-top: #3a3a3c;
    --bg-bottom: #1f1f21;
    --ink: #1b1c1f;
    --ink-soft: #2a2b30;
    --sky: #8cc0e0;
    --sky-deep: #5e9cc6;
    --sky-pale: #d9ebf6;
    --paper: #ffffff;
    --muted: #6d7680;
    --white: #ffffff;
  }
  * { box-sizing: border-box; margin: 0; padding: 0; }
  html, body { width: 1200px; height: 961px; overflow: hidden; }
  body {
    background: radial-gradient(ellipse at 50% 35%, var(--bg-top), var(--bg-bottom) 75%);
    font-family: "Lato", Arial, sans-serif;
    position: relative;
  }
  .piece { position: absolute; box-shadow: 0 10px 30px rgba(0,0,0,.45); overflow: hidden; }

  .wordmark { font-family: "Cinzel", Georgia, serif; font-weight: 400; letter-spacing: .04em; display: flex; align-items: center; gap: 10px; white-space: nowrap; }
  .wordmark .mark-square { background: currentColor; display: inline-block; flex: none; }
  .tagline { font-family: "Cinzel", Georgia, serif; letter-spacing: .35em; }

  /* Soft band standing in for the flowing accent motif */
  .accent-band { position: absolute; left: 0; width: 100%; }
  .accent-band.on-light { background: linear-gradient(180deg, rgba(217,235,246,0) 0%, var(--sky-pale) 45%, var(--sky) 100%); }
  .accent-band.on-dark { background: linear-gradient(180deg, rgba(140,192,224,0) 0%, rgba(94,156,198,.55) 100%); }

  /* Presentation folder */
  .folder { left: 60px; top: 40px; width: 340px; height: 470px;
    background: linear-gradient(180deg, var(--sky-deep) 0%, var(--sky) 35%, var(--sky-pale) 80%, var(--paper) 100%); }
  .folder .brand { position: absolute; top: 190px; left: 0; right: 0; text-align: center; color: var(--white); }
  .folder .wordmark { justify-content: center; font-size: 26px; }
  .folder .wordmark .mark-square { width: 16px; height: 16px; }
  .folder .tagline { margin-top: 8px; font-size: 16px; color: var(--white); }

  /* Letterhead */
  .letterhead { left: 430px; top: 40px; width: 360px; height: 466px; background: var(--paper); }
  .letterhead .header { height: 52px; background: var(--ink); color: var(--white); display: flex; justify-content: space-between; align-items: center; padding: 0 16px; }
  .letterhead .header .wordmark { font-size: 12px; gap: 6px; }
  .letterhead .header .mark-square { width: 8px; height: 8px; }
  .letterhead .contact { font-size: 6.5px; line-height: 1.5; color: #cfd6dc; text-align: right; }
  .letterhead .accent-band { bottom: 24px; height: 34px; }
  .letterhead .footer { position: absolute; bottom: 8px; right: 16px; font-size: 6.5px; color: var(--muted); }

  /* Business cards */
  .card { width: 320px; height: 180px; left: 820px; }
  .card-front { top: 40px; background: var(--ink); color: var(--white); }
  .card-front .wordmark { position: absolute; top: 30px; left: 22px; font-size: 17px; }
  .card-front .wordmark .mark-square { width: 10px; height: 10px; }
  .card-front .tagline { position: absolute; top: 56px; left: 22px; font-size: 9px; color: var(--sky); }
  .card-front .details { position: absolute; top: 30px; right: 20px; font-size: 7.5px; line-height: 1.6; text-align: right; color: #cfd6dc; }
  .card-front .details .doctors { color: var(--white); font-weight: 700; }
  .card-front .accent-band { bottom: 0; height: 34px; }

  .card-back { top: 240px; background: var(--paper); color: var(--ink); padding: 18px 22px; }
  .card-back h3 { font-family: "Cinzel", Georgia, serif; font-weight: 600; font-size: 11px; letter-spacing: .12em; color: var(--ink); }
  .card-back .slot { margin-top: 10px; display: flex; gap: 14px; font-size: 8px; color: var(--muted); }
  .card-back .slot span { flex: 1; border-bottom: 1px solid #b9c2ca; padding-bottom: 3px; }
  .card-back .notice { margin-top: 14px; font-size: 7.2px; line-height: 1.5; color: var(--ink-soft); }
  .card-back .strip { position: absolute; left: 0; bottom: 0; width: 100%; height: 8px; background: var(--sky); }

  /* Envelope */
  .envelope { left: 470px; top: 560px; width: 670px; height: 330px; background: var(--paper); }
  .envelope .flap { position: absolute; left: 0; top: 0; width: 100%; height: 170px; }
  .envelope .flap-brand { position: absolute; top: 34px; left: 0; right: 0; color: var(--white); }
  .envelope .flap-brand .wordmark { justify-content: center; font-size: 14px; }
  .envelope .flap-brand .mark-square { width: 9px; height: 9px; }
  .envelope .return { position: absolute; top: 190px; left: 30px; font-size: 8.5px; line-height: 1.6; color: var(--muted); }
  .envelope .accent-band { bottom: 0; height: 60px; }

  /* Disc */
  .disc { position: absolute; left: 60px; top: 550px; width: 360px; height: 360px; }
</style>
</head>
<body>

<section class="piece folder" aria-label="Presentation folder">
  <div class="brand">
    <div class="wordmark"><span class="mark-square"></span>Maple Hollow</div>
    <div class="tagline">DENTAL CARE</div>
  </div>
</section>

<section class="piece letterhead" aria-label="Letterhead">
  <div class="header">
    <div class="wordmark"><span class="mark-square"></span>Maple Hollow Dental Care</div>
    <div class="contact">
      418 Dunmore Avenue East<br>Kitchener, Ontario N2H 4K7<br>
      Tel 519-555-0142 · Fax 519-555-0143<br>mhdental@brisketmail.example
    </div>
  </div>
  <div class="accent-band on-light" role="img" aria-label="Flowing blue accent motif"></div>
  <div class="footer">www.maplehollowdentalcare.example</div>
</section>

<section class="piece card card-front" aria-label="Business card front">
  <div class="wordmark"><span class="mark-square"></span>Maple Hollow</div>
  <div class="tagline">DENTAL CARE</div>
  <div class="details">
    <div class="doctors">Dr. Mark Esler<br>Dr. Noreen Fadlallah<br>Dr. Beatrice Holloway<br>and Associates</div>
    418 Dunmore Avenue East<br>Kitchener, Ontario N2H 4K7<br>Tel 519-555-0142
  </div>
  <div class="accent-band on-dark" role="img" aria-label="Flowing blue accent motif"></div>
</section>

<section class="piece card card-back" aria-label="Appointment card">
  <h3>Your Appointment</h3>
  <div class="slot"><span>Date</span><span>Time</span></div>
  <p class="notice">This time is reserved just for you. If you are unable to keep this appointment, you are responsible for notifying us immediately at least 24 business hours in advance in which case no charge will be made.</p>
  <div class="strip"></div>
</section>

<section class="piece envelope" aria-label="Envelope">
  <svg class="flap" viewBox="0 0 670 170" preserveAspectRatio="none" aria-hidden="true">
    <polygon points="0,0 670,0 670,40 335,170 0,40" fill="var(--ink)"/>
  </svg>
  <div class="flap-brand">
    <div class="wordmark"><span class="mark-square"></span>Maple Hollow Dental Care</div>
  </div>
  <div class="return">Maple Hollow Dental Care<br>418 Dunmore Avenue East<br>Kitchener, Ontario N2H 4K7</div>
  <div class="accent-band on-light" role="img" aria-label="Flowing blue accent motif"></div>
</section>

<svg class="disc" viewBox="0 0 360 360" aria-label="Disc label">
  <defs>
    <clipPath id="disc-shape"><circle cx="180" cy="180" r="176"/></clipPath>
    <linearGradient id="disc-band" x1="0" y1="0" x2="0" y2="1">
      <stop offset="0" stop-color="#5e9cc6" stop-opacity="0"/>
      <stop offset="1" stop-color="#5e9cc6" stop-opacity=".55"/>
    </linearGradient>
  </defs>
  <circle cx="180" cy="180" r="176" fill="var(--ink)"/>
  <g clip-path="url(#disc-shape)">
    <rect x="0" y="225" width="360" height="60" fill="url(#disc-band)" role="img" aria-label="Flowing blue accent motif"/>
  </g>
  <circle cx="180" cy="180" r="52" fill="#8d9399"/>
  <circle cx="180" cy="180" r="40" fill="var(--ink)"/>
  <circle cx="180" cy="180" r="18" fill="var(--bg-bottom)"/>
  <text x="180" y="96" text-anchor="middle" font-family="Cinzel, Georgia, serif" font-size="16" fill="var(--white)" letter-spacing="1">Maple Hollow Dental Care</text>
</svg>

</body>
</html>
```